Looking for a modern, Professional business card design

We have a simple business card, but are looking for a more modern, professional look. A sample of the basic card is attached as well as the logo. We would also like to add that we offer:
Struggling with your finances?
- Learn to become debt free
- Discover the power of cash
- Control your money instead of it controlling you
Let us help you achieve a new level of financial freedom!
Also, we would like to have a "SPECIAL OFFER!: FREE 30 minute consultation"
Financial Planning

```html
<!DOCTYPE html>
<html lang="en">
<head>
<meta charset="utf-8">
<title>Clearpath Money Coaching – Business Card</title>
<link rel="stylesheet" href="https://fonts.googleapis.com/css2?family=Josefin+Sans:wght@400;600;700&family=Russo+One&display=swap">
<style>
  :root {
    --bg: #e9ecea;
    --card: #ffffff;
    --green-light: #8cc63f;
    --green-dark: #2f8f3a;
    --ink: #1b1b1b;
    --muted: #3a3a3a;
  }
  * { box-sizing: border-box; margin: 0; padding: 0; }
  html, body { width: 1200px; height: 900px; overflow: hidden; }
  body {
    background: var(--bg);
    font-family: "Josefin Sans", sans-serif;
    color: var(--ink);
    position: relative;
  }
  .card {
    position: absolute;
    left: 240px;
    width: 720px;
    height: 411px;
    background: var(--card);
    border-radius: 26px;
    overflow: hidden;
    box-shadow: 0 10px 28px rgba(0,0,0,0.18);
  }
  .card--message { top: 28px; }
  .card--contact { top: 461px; }

  .card__band { position: absolute; left: 0; bottom: 0; width: 100%; height: 40px; }

  /* message side */
  .brand-mark {
    position: absolute; top: 78px; left: 0; width: 100%;
    display: flex; justify-content: center; align-items: center; gap: 14px;
  }
  .brand-mark__dot { width: 26px; height: 26px; border-radius: 50%; background: var(--green-light); }
  .brand-mark__name { font-weight: 700; font-size: 30px; color: var(--ink); letter-spacing: 0.5px; }
  .pitch {
    position: absolute; top: 160px; left: 0; width: 100%;
    text-align: center; font-size: 21px; line-height: 31px; color: var(--muted);
  }
  .pitch__head { font-size: 21px; letter-spacing: 0.5px; color: var(--ink); }
  .accent { color: var(--green-light); }
  .accent-strong { color: var(--green-light); font-weight: 700; }

  /* contact side */
  .logo-lockup {
    position: absolute; top: 150px; left: 52px;
    display: flex; align-items: center; gap: 12px;
  }
  .logo-lockup__dot { width: 20px; height: 20px; border-radius: 50%; background: var(--green-light); }
  .logo-lockup__name { font-weight: 700; font-size: 22px; color: var(--ink); white-space: nowrap; }
  .identity { position: absolute; top: 66px; right: 50px; text-align: right; }
  .identity__name {
    font-family: "Russo One", sans-serif; font-size: 30px; font-weight: 400;
    color: var(--green-light); letter-spacing: 1px; white-space: nowrap;
  }
  .identity__title {
    font-family: "Russo One", sans-serif; font-size: 14px; color: var(--ink);
    letter-spacing: 0.5px; margin-top: 4px; padding-bottom: 8px;
    border-bottom: 2px solid var(--green-dark); display: inline-block; padding-left: 24px;
    white-space: nowrap;
  }
  .offer { margin-top: 14px; font-size: 20px; line-height: 24px; color: var(--green-light); white-space: nowrap; }
  .offer__label { font-family: "Russo One", sans-serif; font-size: 15px; }
  .offer__free { color: var(--ink); font-weight: 700; }
  .divider {
    position: absolute; left: 46px; right: 46px; top: 238px;
    height: 2px; background: var(--green-dark);
  }
  .contacts { position: absolute; left: 52px; top: 256px; list-style: none; }
  .contacts li {
    display: flex; align-items: center; gap: 16px;
    font-size: 21px; line-height: 34px; color: var(--ink); white-space: nowrap;
  }
  .contacts svg { width: 18px; height: 18px; flex: none; }
  .contacts .web-domain { color: var(--green-light); }
</style>
</head>
<body>

<section class="card card--message" aria-label="Card back: services message">
  <div class="brand-mark">
    <span class="brand-mark__dot"></span>
    <span class="brand-mark__name">Clearpath Money Coaching</span>
  </div>
  <div class="pitch">
    <p class="pitch__head"><span class="accent">STRUGGLING</span> WITH YOUR <span class="accent-strong">FINANCES?</span></p>
    <p>Learn to become debt free</p>
    <p>Discover the power of cash</p>
    <p>Control your money instead of it controlling you</p>
    <p>Let us help you achieve a new level of financial <span class="accent-strong">FREEDOM!</span></p>
  </div>
  <svg class="card__band" viewBox="0 0 720 40" preserveAspectRatio="none" aria-hidden="true">
    <rect x="0" y="26" width="720" height="14" fill="var(--green-dark)"/>
    <polygon points="380,14 720,14 720,40 372,40" fill="var(--green-light)"/>
    <rect x="0" y="22" width="380" height="4" fill="var(--green-dark)"/>
  </svg>
</section>

<section class="card card--contact" aria-label="Card front: contact details">
  <div class="logo-lockup">
    <span class="logo-lockup__dot"></span>
    <span class="logo-lockup__name">Clearpath Money Coaching</span>
  </div>
  <div class="identity">
    <h1 class="identity__name">DANIEL R. HAYES</h1>
    <p class="identity__title">PERSONAL FINANCIAL COACH</p>
    <p class="offer"><span class="offer__label">SPECIAL OFFER!</span> <span class="offer__free">FREE 30</span><br>minute consultation</p>
  </div>
  <div class="divider"></div>
  <ul class="contacts">
    <li>
      <svg viewBox="0 0 18 18" aria-hidden="true"><rect x="4" y="1" width="10" height="16" rx="2" fill="none" stroke="var(--green-light)" stroke-width="1.8"/><circle cx="9" cy="14" r="1.1" fill="var(--green-light)"/></svg>
      (555) 014-2288
    </li>
    <li>
      <svg viewBox="0 0 18 18" aria-hidden="true"><rect x="1.5" y="4" width="15" height="10" fill="none" stroke="var(--green-light)" stroke-width="1.8"/><polyline points="1.5,4 9,10 16.5,4" fill="none" stroke="var(--green-light)" stroke-width="1.8"/></svg>
      daniel@clearpathmoneyhelp.com
    </li>
    <li>
      <svg viewBox="0 0 18 18" aria-hidden="true"><circle cx="9" cy="9" r="7.5" fill="none" stroke="var(--green-light)" stroke-width="1.6"/><ellipse cx="9" cy="9" rx="3.2" ry="7.5" fill="none" stroke="var(--green-light)" stroke-width="1.3"/><line x1="1.5" y1="9" x2="16.5" y2="9" stroke="var(--green-light)" stroke-width="1.3"/></svg>
      <span>www.<span class="web-domain">clearpathmoneyhelp</span>.com</span>
    </li>
  </ul>
  <svg class="card__band" viewBox="0 0 720 40" preserveAspectRatio="none" aria-hidden="true">
    <rect x="0" y="26" width="720" height="14" fill="var(--green-dark)"/>
    <polygon points="480,14 720,14 720,40 472,40" fill="var(--green-light)"/>
    <rect x="0" y="22" width="480" height="4" fill="var(--green-dark)"/>
  </svg>
</section>

</body>
</html>
```